Design for a Service-Based Estimate

We want a design for an Estimate that will always be sent in PDF format. The estimate or proposal is a critical document that needs to plainly show the service items, item description but also needs to be attractive and professional looking. Our current estimate deliverable is attached but it looks really basic like a Word document

```html
<!DOCTYPE html>
<html lang="en">
<head>
<meta charset="utf-8">
<title>Estimate – Stoneline Paving</title>
<link href="https://fonts.googleapis.com/css2?family=Open+Sans:ital,wght@0,400;0,600;0,800;1,400&display=swap" rel="stylesheet">
<style>
:root{
  --navy:#363150;
  --red:#d04a2f;
  --grey:#8a827b;
  --rule:#8f8780;
  --text:#5f5a56;
  --faint-navy:#e3e2e8;
  --bg:#f4f4f4;
  --paper:#ffffff;
}
*{box-sizing:border-box;margin:0;padding:0}
html,body{width:849px;height:1200px;overflow:hidden}
body{background:var(--bg);font-family:"Open Sans",sans-serif;color:var(--text);position:relative}
.page{position:absolute;background:var(--paper);border:1px solid #e2e2e2;overflow:hidden}
.page--estimate{left:36px;top:44px;width:434px;height:628px}
.page--terms{left:395px;top:529px;width:417px;height:626px}
.abs{position:absolute}
.wordmark{position:absolute;font-family:"Open Sans",sans-serif;font-weight:800;color:var(--navy);font-size:20px;letter-spacing:1px;white-space:nowrap;display:flex;align-items:center;gap:7px}
.wordmark__dot{width:11px;height:11px;background:var(--red)}
.wordmark--faint{color:var(--faint-navy);font-size:28px}
.rule{position:absolute;height:2px;background:var(--rule)}
.band{position:absolute;background:var(--navy)}
.accent{position:absolute;background:var(--red)}

/* estimate page */
.recipient__label{font-size:8px;left:14px;top:90px}
.recipient__name{font-size:13px;color:var(--navy);left:14px;top:102px}
.recipient__line{font-size:8.5px;left:14px}
.date{font-size:8.5px;right:27px;top:103px}
.project{left:0;width:434px;top:172px;text-align:center;font-size:8.5px;line-height:11px}
.project__title{color:var(--red);font-size:10.5px;line-height:12px}
.estimate-table{position:absolute;left:14px;top:216px;width:393px;border-collapse:collapse;font-size:7.5px}
.estimate-table th,.estimate-table td{border:1px solid var(--rule);text-align:center;vertical-align:middle}
.estimate-table th{color:var(--red);font-weight:400;font-size:11px;height:37px;line-height:12px}
.estimate-table th.col-item{text-align:left;padding-left:5px}
.estimate-table td.item{text-align:left;padding:0 5px;line-height:9.3px}
.estimate-table td.amount{color:var(--red);font-size:9.5px;font-weight:600}
.col-item{width:202px}.col-n{width:48px}
.row-main td{height:80px}.row-opt td{height:37px}
.total-box{position:absolute;left:311px;top:370px;width:96px;height:36px;border:1px solid var(--rule);border-top:none;color:var(--red);font-size:9.5px;display:flex;align-items:center;justify-content:center;gap:5px}

/* terms page */
.terms__title{left:0;width:417px;padding-left:20px;text-align:center;top:93px;font-size:10.5px;color:var(--navy);font-weight:600}
.terms__list{position:absolute;left:25px;top:117px;width:380px;list-style:none;font-size:6.8px;line-height:8.9px}
.terms__list li{position:relative;margin-bottom:8.8px}
.terms__list li.tick::before{content:"";position:absolute;left:-15px;top:4px;width:10px;height:1px;background:var(--paper)}
.signature__mark{left:-3px;top:360px;width:152px;height:42px;background:linear-gradient(90deg,#e9e7e5,#f5f4f3)}
.signature__line{left:20px;top:406px;width:103px;height:1.5px;background:var(--rule)}
.signature__label{left:20px;width:103px;top:410px;text-align:center;font-style:italic;font-size:10px;color:var(--grey)}
</style>
</head>
<body>

<section class="page page--estimate">
  <div class="wordmark" style="left:126px;top:22px"><span class="wordmark__dot"></span>STONELINE PAVING</div>
  <div class="rule" style="left:14px;top:74px;width:393px"></div>

  <p class="abs recipient__label">To:</p>
  <p class="abs recipient__name">Dana Whitfield</p>
  <p class="abs recipient__line" style="top:124px">42 Harbor Lane se Marlow 30218</p>
  <p class="abs recipient__line" style="top:135px">dwhitfield@mailbox.com</p>
  <p class="abs date">Date:</p>

  <div class="abs project">
    <p class="project__title">Dana Whitfield New Concrete Pad</p>
    <p>42 Harbor Lane SE Marlow 30218</p>
    <p>Bid#: 20-0182</p>
  </div>

  <table class="estimate-table">
    <tr>
      <th class="col-item">Item</th><th class="col-n">Quantity</th><th class="col-n">U/M</th><th class="col-n">Unit<br>$</th><th>Total: $</th>
    </tr>
    <tr class="row-main">
      <td class="item">Form, Pour &amp; Finish New Concrete Slab (24′ x 24′ x 4″).<br><br>Includes:<br>3000psi Concrete Mix,<br>Footer (12″ x 8″) with One Continous Rebar,<br>Wire Mesh Reinforcement and Saw-Cut Expansion Joints</td>
      <td>576</td><td>SF</td><td>$8.65</td><td class="amount">$4,982.40</td>
    </tr>
    <tr class="row-opt">
      <td class="item">OPTIONAL: Add (2′ x 24″ x 4″) Small Ramp Area</td>
      <td>48</td><td>SF</td><td>$8.65</td><td class="amount">$415.20</td>
    </tr>
  </table>
  <div class="total-box"><span>Total Price</span><span>$5,397.60</span></div>

  <div class="wordmark wordmark--faint" style="left:75px;top:545px">STONELINE PAVING</div>
  <div class="rule" style="left:14px;top:593px;width:316px"></div>
</section>
<div class="band" style="left:24px;top:647px;width:342px;height:25px"></div>

<section class="page page--terms">
  <div class="accent" style="left:0;top:2px;width:20px;height:341px"></div>
  <div class="wordmark" style="left:126px;top:26px"><span class="wordmark__dot"></span>STONELINE PAVING</div>
  <div class="rule" style="left:20px;top:79px;width:373px"></div>

  <p class="abs terms__title">Terms and Conditions</p>
  <ul class="terms__list">
    <li class="tick">Prices as quoted in this estimate are valid for (60) days only.</li>
    <li class="tick">Payment in full, less any previously paid amounts, is due to the Contractor upon completion of the proposed scope of work.</li>
    <li class="tick">All change order requests must be communicated in writting to the Contractor by the Client or their authorized representative.</li>
    <li class="tick">All measurements listed in this estimate are approximate and may vary slightly due to actual field conditions.</li>
    <li class="tick">It is agreed by the Contractor and the Client that complications and costs arising from unforeseen conditions and handling of unsuitable materials are not included in this estimate.</li>
    <li class="tick">Unless specifically listed in this estimate, the following items and their costs are not included: Maintenance of Traffic, Concrete Material Pumping, Testing, Excavation, Grading and Fill Material, Permits and Fees, Surveying and As-builts, Irrigation Repair, Landscaping and Root Mitigation, De-watering, Private Locates and Accessibility.</li>
    <li>Private utility locating services using radio detection devices and, when necessary, ground penetrating radar are offered by Stoneline Paving to assist in finding private utilities that may not have been located by the public one call system. Stoneline Paving will not be responsible for private utilities that have not been located nor for the failure of the above equipment to accurately detect existing utilities since the equipment is fallible and existing site conditions may preclude the ability of the equipment to detect an identifiable signal.</li>
  </ul>

  <div class="abs signature__mark" role="img" aria-label="Handwritten client signature"></div>
  <div class="abs signature__line"></div>
  <p class="abs signature__label">Client Signature</p>

  <div class="wordmark wordmark--faint" style="left:40px;top:548px">STONELINE PAVING</div>
  <div class="rule" style="left:0;top:598px;width:374px"></div>
  <div class="accent" style="left:374px;top:524px;width:19px;height:84px"></div>
  <div class="band" style="left:-1px;top:608px;width:417px;height:18px"></div>
</section>

</body>
</html>
```